luxury contemporary fashion website needs simple, elegant flowchart to describe the buying and selli

* Luxury, resale, preloved items are sold on this online platform
*Horizontal, simple, flowchart with 5 steps in 'friendly' font with a simple emoticon/ picture for each step
*To be positioned in the 'How we work' tab of the webpage to explain in a very simple manner the buying and selling process for the customers.
*Attached is a very rudimentary mock-up of what we would like included and an idea of a project similar to what we desire
* to confirm the text for each step, we have also attached a word file below

Industry/Entity Type

Fashion

Font styles to use
Sans Serif

Colors
86cfc6
cfeae6

Requirements
Must have
• Simple drawing / shape after each point In the closest to 'duck egg blue' fill colour you can find with a black outline

```html
<!DOCTYPE html>
<html lang="en">
<head>
<meta charset="utf-8">
<title>Bespoke Personal Concierge – How we work</title>
<link rel="stylesheet" href="https://fonts.googleapis.com/css2?family=Quicksand:wght@300;400;500&family=Nunito:wght@800&display=swap">
<style>
  :root {
    --teal: #86cfc6;
    --teal-pale: #cfeae6;
    --ink: #111111;
    --paper: #ffffff;
  }
  * { box-sizing: border-box; margin: 0; padding: 0; }
  html, body { width: 1200px; height: 480px; overflow: hidden; background: var(--paper); }
  .canvas { position: relative; width: 1200px; height: 480px; font-family: "Quicksand", sans-serif; font-weight: 500; color: var(--ink); }
  .shapes { position: absolute; inset: 0; }
  .title {
    position: absolute; top: 40px; left: 0; width: 1200px; text-align: center;
    font-family: "Quicksand", sans-serif; font-weight: 300; font-size: 35px;
    color: var(--teal); letter-spacing: 0;
  }
  .step-heading {
    position: absolute; width: 200px; text-align: center;
    font-family: "Nunito", sans-serif; font-weight: 800; font-size: 20px; line-height: 28px;
  }
  .step-text {
    position: absolute; width: 200px; text-align: center;
    font-size: 17px; line-height: 24px;
  }
  .payment-label {
    position: absolute; left: 845px; top: 218px; width: 190px; text-align: center;
    font-family: "Nunito", sans-serif; font-weight: 800; font-size: 20px; color: var(--teal);
  }
  .outcome { position: absolute; text-align: center; font-size: 21px; line-height: 27px; text-transform: uppercase; }
  .outcome-note { display: block; font-size: 17px; text-transform: none; line-height: 24px; }
</style>
</head>
<body>
<main class="canvas">
  <svg class="shapes" width="1200" height="480" viewBox="0 0 1200 480" aria-hidden="true">
    <defs>
      <path id="step-cloud" d="M12 28 C3 28 2 17 9 15 C8 6 19 3 23 9 C26 1 38 3 38 11 C47 11 49 23 41 26 C40 29 36 29 34 28 Z"
            fill="none" stroke="var(--ink)" stroke-width="1.6"/>
      <marker id="arrow-head" viewBox="0 0 10 10" refX="6" refY="5" markerWidth="5" markerHeight="5" orient="auto">
        <path d="M0 0 L10 5 L0 10 Z" fill="var(--teal)"/>
      </marker>
    </defs>

    <g font-family="Nunito, sans-serif" font-weight="800" font-size="15" text-anchor="middle">
      <use href="#step-cloud" x="79" y="106"/><text x="104" y="130">1</text>
      <use href="#step-cloud" x="266" y="106"/><text x="291" y="130">2</text>
      <use href="#step-cloud" x="479" y="110"/><text x="504" y="134">3</text>
      <use href="#step-cloud" x="684" y="110"/><text x="709" y="134">4</text>
      <use href="#step-cloud" x="914" y="110"/><text x="939" y="134">5</text>
    </g>

    <g class="icon-stars" fill="var(--teal)" stroke="var(--ink)" stroke-width="1" stroke-linejoin="round">
      <path d="M166 284 l2.5 5 5.5 .8 -4 3.9 1 5.5 -5 -2.6 -5 2.6 1 -5.5 -4 -3.9 5.5 -.8z"/>
      <path d="M178 278 l2 4 4.4 .6 -3.2 3.1 .8 4.4 -4 -2.1 -4 2.1 .8 -4.4 -3.2 -3.1 4.4 -.6z"/>
      <path d="M175 291 l2 4 4.4 .6 -3.2 3.1 .8 4.4 -4 -2.1 -4 2.1 .8 -4.4 -3.2 -3.1 4.4 -.6z"/>
    </g>

    <path class="icon-heart" d="M357 350 C340 338 343 325 351 325 C355 325 357 328 357 330 C357 328 359 325 363 325 C371 325 374 338 357 350 Z"
          fill="var(--teal)" stroke="var(--ink)" stroke-width="1.4"/>

    <!-- checked badge -->
    <g class="icon-check">
      <circle cx="597" cy="360" r="11" fill="var(--teal)" stroke="var(--ink)" stroke-width="1.4"/>
      <path d="M591.5 360.5 L595.5 364.5 L602.5 355.5" fill="none" stroke="var(--ink)" stroke-width="1.8" stroke-linecap="round" stroke-linejoin="round"/>
    </g>

    <!-- aeroplane -->
    <g class="icon-plane" fill="var(--teal-pale)" stroke="var(--ink)" stroke-width="1.3" stroke-linejoin="round" transform="rotate(-12 811 316)">
      <path d="M806 311 L800 300 L805 300 L815 311 Z"/>
      <path d="M806 320 L800 331 L805 331 L815 320 Z"/>
      <path d="M795 311 L791 305 L794 305 L799 311 Z"/>
      <path d="M793 311 L823 311 C830 311 832 315.5 832 315.5 C832 315.5 830 320 823 320 L793 320 C791 320 791 311 793 311 Z"/>
    </g>

    <path class="payment-cloud"
          d="M880 300 C845 300 838 255 862 245 C850 200 905 180 925 205 C940 160 1010 170 1010 205 C1045 205 1050 250 1025 262 C1032 290 1000 305 985 295 C970 312 930 312 915 298 Z"
          fill="var(--paper)" stroke="var(--teal)" stroke-width="6" stroke-linejoin="round"/>

    <path d="M1020 268 Q1050 260 1086 272" fill="none" stroke="var(--teal)" stroke-width="4" stroke-linecap="round" marker-end="url(#arrow-head)"/>
    <path d="M958 306 Q958 345 968 370" fill="none" stroke="var(--teal)" stroke-width="4" stroke-linecap="round" marker-end="url(#arrow-head)"/>

    <g font-family="Nunito, sans-serif" font-weight="800" fill="var(--teal)" stroke="var(--ink)" stroke-width="0.8" text-anchor="middle">
      <text x="1158" y="220" font-size="22">$</text>
      <text x="1139" y="240" font-size="20">£</text>
      <text x="1165" y="247" font-size="18">€</text>
    </g>

    <!-- charity badge with halo and heart -->
    <g class="icon-charity">
      <ellipse cx="1108" cy="366" rx="10" ry="3" fill="none" stroke="var(--ink)" stroke-width="1.2"/>
      <circle cx="1108" cy="382" r="13" fill="var(--teal)" stroke="var(--ink)" stroke-width="1.4"/>
      <path d="M1108 388 C1101 383 1102 377 1105 377 C1107 377 1108 379 1108 380 C1108 379 1109 377 1111 377 C1114 377 1115 383 1108 388 Z"
            fill="var(--paper)" stroke="var(--ink)" stroke-width="1"/>
    </g>
  </svg>

  <h1 class="title">BESPOKE PERSONAL CONCIERGE</h1>

  <h2 class="step-heading" style="left:3px; top:161px;">Have items<br>to sell ?</h2>
  <p class="step-text" style="left:3px; top:233px;">- brand spanking<br>or nearly<br>new</p>

  <h2 class="step-heading" style="left:190px; top:161px;">Personal<br>collection</h2>
  <p class="step-text" style="left:188px; top:233px;">- we choose the<br>pieces we know<br>the lumaro<br>customers<br>will love</p>

  <h2 class="step-heading" style="left:403px; top:161px;">We Prepare</h2>
  <p class="step-text" style="left:397px; top:233px;">- your item for sale<br>with thorough<br>autheticity<br>&amp; condition checks...<br>so&nbsp; you<br>don't have to !</p>

  <h2 class="step-heading" style="left:608px; top:161px;">Once sold</h2>
  <p class="step-text" style="left:608px; top:233px;">-we lovingly<br>prepare the item</p>
  <p class="step-text" style="left:608px; top:286px;">- shipped via<br>tracked services</p>

  <p class="payment-label">Your payment</p>

  <p class="outcome" style="left:1082px; top:259px; width:120px;">Pocket<br>the cash</p>
  <p class="outcome" style="left:865px; top:378px; width:230px;">Donate to charity<span class="outcome-note">(full or partial amount)</span></p>
</main>
</body>
</html>
```